Finiding oppertunites in Real Estate 6.15.20

size of ad 7” x 9.6”
1-I like the ad to stand out and attract people's attention.
2-you should be able to see the text of the ad clearly .. see the attachment anything in yellow is instructions.
3-the list of topics should not be the main part of the ad
4-if you decide you want a picture or vector of a person .. (you decide)
then it should be a white male about 25-30 years old wearing a solid white or blue shirt and not long hair.
5-leave 1 inch for footer
see attachment
Good luck

Target Market(s)

potential male students 25-35 years of age

Industry/Entity Type

Education

Requirements
Must have
• will stand out and people would want to see it.
should be able to read the words of ad
Nice to have
• how to make money in real estate on one line

```html
<!DOCTYPE html>
<html lang="en">
<head>
<meta charset="utf-8">
<title>Real Estate Career Course</title>
<link rel="stylesheet" href="https://fonts.googleapis.com/css2?family=Playfair+Display:wght@600&family=Montserrat:wght@400;500;600;700&display=swap">
<style>
  :root {
    --plum: #6b2a6e;
    --violet: #8a3a86;
    --magenta: #a8457f;
    --night: #1e1c4a;
    --panel: #25204f;
    --gold: #f0c23a;
    --white: #ffffff;
    --soft: #eae4f1;
  }
  * { margin: 0; padding: 0; box-sizing: border-box; }
  html, body { width: 875px; height: 1200px; overflow: hidden; background: var(--night); }
  .ad {
    position: relative;
    width: 875px;
    height: 1200px;
    overflow: hidden;
    font-family: "Montserrat", Arial, sans-serif;
    color: var(--white);
  }
  .top-band { position: absolute; left: 0; top: 0; width: 875px; height: 36px; background: var(--night); }
  .city-backdrop {
    position: absolute; left: 0; top: 36px; width: 875px; height: 1037px;
    background:
      radial-gradient(ellipse at 78% 35%, rgba(214,96,140,.55), transparent 55%),
      linear-gradient(180deg, #5e2a6c 0%, var(--violet) 35%, var(--plum) 65%, #3c2660 100%);
  }
  .presenter-photo {
    position: absolute; left: 465px; top: 165px; width: 355px; height: 446px;
    background: linear-gradient(180deg, rgba(240,210,200,.25) 0%, #2a2a3a 45%, #1b1b26 100%);
    border-radius: 150px 150px 0 0;
  }
  .title {
    position: absolute; left: 0; top: 48px; width: 875px; text-align: center;
    font-family: "Playfair Display", Georgia, serif; font-weight: 600;
    font-size: 94px; letter-spacing: 1px; line-height: 1;
  }
  .subtitle {
    position: absolute; left: 0; top: 158px; width: 875px; text-align: center;
    font-size: 38px; font-weight: 500; letter-spacing: 10px; line-height: 1;
  }
  .sessions {
    position: absolute; left: 82px; top: 272px;
    color: var(--gold); font-weight: 700; font-size: 54px; line-height: 1.12;
  }
  .session-count {
    position: absolute; left: 82px; top: 408px; font-size: 31px; font-weight: 700;
  }
  .divider { position: absolute; left: 82px; top: 467px; width: 392px; height: 3px; background: var(--white); }
  .start-date {
    position: absolute; left: 82px; top: 490px; font-size: 33px; font-weight: 700; line-height: 1.12;
  }
  .pitch {
    position: absolute; left: 42px; top: 611px; width: 795px; height: 254px;
    background: var(--panel); border-radius: 18px; text-align: center; padding-top: 34px;
  }
  .pitch h2 { color: var(--gold); font-size: 28px; font-weight: 700; margin-bottom: 18px; }
  .pitch p { font-size: 25px; line-height: 1.25; margin-bottom: 12px; }
  .topics-label {
    position: absolute; left: 0; top: 898px; width: 875px; text-align: center;
    font-size: 15px; font-weight: 700; letter-spacing: .5px;
  }
  .topics {
    position: absolute; top: 936px; list-style: none; font-size: 18px; line-height: 22px; color: var(--soft);
  }
  .col-a { left: 101px; } .col-b { left: 358px; } .col-c { left: 620px; }
  .footer-band { position: absolute; left: 0; top: 1073px; width: 875px; height: 127px; background: var(--night); }
</style>
</head>
<body>
<div class="ad">
  <div class="top-band"></div>
  <div class="city-backdrop" role="img" aria-label="Purple-tinted city skyline at dusk"></div>
  <div class="presenter-photo" role="img" aria-label="Smiling young man in dark suit and tie holding a clipboard"></div>

  <h1 class="title">REAL ESTATE</h1>
  <div class="subtitle">CAREER COURSE</div>

  <div class="sessions">REMOTE<br>SESSIONS</div>
  <div class="session-count">12 SESSION COURSE</div>
  <div class="divider"></div>
  <div class="start-date">CLASSES STARTING<br>JUNE 16</div>

  <section class="pitch">
    <h2>HOW TO MAKE MONEY IN REAL ESTATE?</h2>
    <p>For those who have started or would like<br>to go into Real Estate</p>
    <p>An investment in knowledge opens up<br>untold opportunities</p>
  </section>

  <div class="topics-label">A PARTIAL LISTING OF TOPICS:</div>
  <ul class="topics col-a">
    <li>Single-family</li><li>Multifamily</li><li>Management</li><li>Real Estate Concepts</li><li>Real Estate law</li>
  </ul>
  <ul class="topics col-b">
    <li>Investment properties</li><li>Foreclosures</li><li>Rehab</li><li>Foreclosures</li><li>Short sales</li>
  </ul>
  <ul class="topics col-c">
    <li>Development</li><li>Finical modeling</li><li>HUD properties</li><li>Due Diligence e</li>
  </ul>

  <div class="footer-band"></div>
</div>
</body>
</html>
```